The Harvest Compass

Cutting Through the Noise to What Actually Works.

Nutrition book

Target Market(s)

People looking to be or get healthy and eat right.

```html
<!DOCTYPE html>
<html lang="en">
<head>
<meta charset="utf-8">
<title>The Harvest Compass — Book Cover</title>
<link rel="stylesheet" href="https://fonts.googleapis.com/css2?family=Oswald:wght@300;600&family=Jost:wght@500&display=swap">
<style>
  :root {
    --paper: #ffffff;
    --slate: #555e78;
    --blue: #3f5898;
    --food-top: #f3c623;
    --food-mid: #e98a3a;
    --food-low: #d9b56e;
    --food-base: #6fb23a;
  }
  html, body {
    margin: 0;
    padding: 0;
    overflow: hidden;
    background: var(--paper);
  }
  .cover {
    position: relative;
    width: 800px;
    height: 1200px;
    overflow: hidden;
    background: var(--paper);
  }
  .title {
    position: absolute;
    left: 0;
    top: 0;
    width: 800px;
    height: 520px;
  }
  .title-thin {
    font-family: "Oswald", sans-serif;
    font-weight: 300;
    fill: var(--slate);
  }
  .title-bold {
    font-family: "Oswald", sans-serif;
    font-weight: 600;
    fill: var(--blue);
  }
  .tagline {
    position: absolute;
    left: 342px;
    top: 57px;
    margin: 0;
    font-family: "Jost", sans-serif;
    font-weight: 500;
    font-size: 31px;
    line-height: 36px;
    letter-spacing: 0.19em;
    text-transform: uppercase;
    color: var(--slate);
  }
  .food-pyramid {
    position: absolute;
    left: 100px;
    top: 522px;
    width: 598px;
    height: 602px;
  }
  .author {
    position: absolute;
    left: 0;
    width: 800px;
    top: 1128px;
    margin: 0;
    text-align: center;
    font-family: "Jost", sans-serif;
    font-weight: 500;
    font-size: 44px;
    letter-spacing: 0.3em;
    text-indent: 0.3em;
    color: var(--slate);
  }
</style>
</head>
<body>
<main class="cover">
  <svg class="title" viewBox="0 0 800 520" aria-label="The Harvest Compass">
    <text class="title-thin" x="41" y="174" font-size="136" textLength="217" lengthAdjust="spacingAndGlyphs">THE</text>
    <text class="title-bold" x="54" y="347" font-size="174" textLength="691" lengthAdjust="spacingAndGlyphs">HARVEST</text>
    <text class="title-thin" x="54" y="500" font-size="140" textLength="690" lengthAdjust="spacingAndGlyphs">COMPASS</text>
  </svg>

  <p class="tagline">Cutting through<br>the noise to what<br>actually works</p>

  <svg class="food-pyramid" viewBox="0 0 598 602" role="img" aria-label="Illustrated food pyramid: oils and nuts at the top, proteins, dairy, grains and breads, with vegetables and fruits forming the wide base">
    <defs>
      <linearGradient id="pyramid-tones" x1="0" y1="0" x2="0" y2="1">
        <stop offset="0" stop-color="var(--food-top)"/>
        <stop offset="0.35" stop-color="var(--food-mid)"/>
        <stop offset="0.65" stop-color="var(--food-low)"/>
        <stop offset="1" stop-color="var(--food-base)"/>
      </linearGradient>
    </defs>
    <polygon points="299,0 598,602 0,602" fill="url(#pyramid-tones)" opacity="0.85"/>
  </svg>

  <p class="author">Author Name</p>
</main>
</body>
</html>
```